Income Tax Flyer - Updates Needed

Just need to update this flyer design and give it a new look. We would like to keep all the same wording but make it stand out a little more. Our selling point is the "Same Day Tax Advance up to $6,000"

Industry/Entity Type

Lending, Small Loans, Tax Services, Title Loans, Personal Loans

```html
<!DOCTYPE html>
<html lang="en">
<head>
<meta charset="utf-8">
<title>Same Day Tax Advance Flyer</title>
<link rel="stylesheet" href="https://fonts.googleapis.com/css2?family=Barlow+Condensed:wght@700;800&family=Poppins:wght@500;600;700;800&display=swap">
<style>
:root{
  --green:#0f5a34;
  --green-deep:#0a4327;
  --red:#c81f27;
  --white:#ffffff;
  --ink:#1b1b1b;
  --stage:#061a10;
  --photo-warm:#b9a98f;
  --photo-light:#d9d4cb;
}
html,body{margin:0;padding:0;width:1200px;height:2500px;overflow:hidden;background:var(--stage);}
.flyer{position:absolute;left:120px;top:629px;width:768px;height:994px;transform:scale(1.25);transform-origin:0 0;background:var(--white);overflow:hidden;font-family:"Poppins",sans-serif;}
.shapes{position:absolute;inset:0;width:768px;height:994px;}
.abs{position:absolute;margin:0;}
.brand{left:62px;top:88px;color:var(--white);font-family:"Poppins",sans-serif;font-weight:600;font-size:30px;line-height:1;letter-spacing:.5px;}
.headline{left:62px;top:222px;font-family:"Barlow Condensed",sans-serif;font-weight:800;font-size:60px;line-height:60px;color:var(--white);letter-spacing:.5px;}
.headline .amount{background:var(--red);padding:0 8px 0 4px;}
.offer-lead{left:70px;top:488px;color:var(--white);font-weight:700;font-size:33px;line-height:37px;}
.offer-lead strong{display:block;font-weight:800;font-size:42px;line-height:40px;letter-spacing:.5px;}
.selling-point{left:440px;top:527px;font-family:"Barlow Condensed",sans-serif;font-weight:800;color:var(--green);font-size:45px;line-height:42px;}
.selling-point .big{color:var(--red);font-size:62px;line-height:62px;display:block;}
.feature-label{top:802px;width:220px;text-align:center;color:var(--ink);font-weight:600;font-size:20px;line-height:23px;}
.call{left:92px;top:867px;color:var(--white);font-family:"Barlow Condensed",sans-serif;font-weight:700;font-size:36px;line-height:40px;}
.branch{top:929px;color:var(--white);font-size:13px;line-height:15px;font-weight:500;padding-left:14px;}
.branch b{display:block;font-weight:700;}
</style>
</head>
<body>
<main class="flyer">
  <svg class="shapes" viewBox="0 0 768 994" xmlns="http://www.w3.org/2000/svg">
    <defs>
      <linearGradient id="photoFade" x1="0" x2="1" y1="0" y2="0">
        <stop offset="0" stop-color="#0f5a34"/>
        <stop offset=".35" stop-color="#0f5a34"/>
        <stop offset=".6" stop-color="#6f7f6c"/>
        <stop offset="1" stop-color="#d9d4cb"/>
      </linearGradient>
      <linearGradient id="insetFill" x1="0" x2="1" y1="0" y2="1">
        <stop offset="0" stop-color="#e8e6e2"/>
        <stop offset="1" stop-color="#a9a7a2"/>
      </linearGradient>
    </defs>
    <rect class="hero-photo" role="img" aria-label="Photo of two happy people giving a high five in a bright office" x="0" y="0" width="768" height="500" fill="url(#photoFade)"/>
    <polygon points="438,482 768,455 768,994 0,994 0,668 395,668" fill="#ffffff"/>
    <polygon points="250,450 400,355 438,430" fill="#ffffff"/>
    <polygon class="offer-band" points="0,482 438,428 395,668 0,668" fill="#c81f27"/>
    <line x1="428" y1="318" x2="414" y2="430" stroke="#fff" stroke-width="3"/>
    <line x1="356" y1="526" x2="335" y2="628" stroke="#fff" stroke-width="3"/>
    <circle cx="574" cy="428" r="96" fill="#c81f27"/>
    <circle class="inset-photo" role="img" aria-label="Photo of a hand using a calculator beside paperwork" cx="574" cy="428" r="86" fill="url(#insetFill)" stroke="#fff" stroke-width="4"/>
    <g fill="none" stroke="#0f5a34" stroke-width="1.5" stroke-dasharray="10 6">
      <circle cx="162" cy="738" r="58"/><circle cx="396" cy="738" r="58"/><circle cx="624" cy="738" r="58"/>
    </g>
    <g fill="#0f5a34"><circle cx="162" cy="738" r="47"/><circle cx="396" cy="738" r="47"/><circle cx="624" cy="738" r="47"/></g>
    <g stroke="#0f5a34" stroke-width="2"><line x1="232" y1="738" x2="324" y2="738"/><line x1="465" y1="738" x2="557" y2="738"/></g>
    <g fill="#c81f27"><circle cx="278" cy="738" r="3.5"/><circle cx="511" cy="738" r="3.5"/></g>
    <g fill="none" stroke="#fff" stroke-width="4" stroke-linecap="round" stroke-linejoin="round">
      <path d="M142 722c-4 10 4 26 18 34l6-8-8-6-4 4c-5-3-9-9-10-14l4-3-4-9z" fill="#fff" stroke-width="2"/>
      <circle cx="172" cy="730" r="16" stroke-width="3"/><path d="M172 721v9l6 4" stroke-width="3"/>
      <circle cx="381" cy="723" r="11" stroke-width="3"/><circle cx="411" cy="723" r="11" stroke-width="3"/>
      <path d="M386 740h20l6 22h-32z" stroke-width="3"/>
      <path d="M606 740l10 12 22-26" stroke-width="6"/>
    </g>
    <g font-family="Poppins,sans-serif" font-weight="700" font-size="13" fill="#fff" text-anchor="middle">
      <text x="381" y="728">$</text><text x="411" y="728">$</text><text x="396" y="758" fill="#fff">$</text>
    </g>
    <polygon class="footer-band" points="0,850 768,938 768,994 0,994" fill="#0f5a34"/>
    <polygon points="672,938 768,920 768,948" fill="#c81f27"/>
    <path d="M0 866h380a20 20 0 0 1 0 40H0z" fill="#c81f27"/>
    <path d="M62 878c-3 8 3 20 13 26l5-6-6-5-3 3c-4-2-7-6-8-10l3-2-3-7z" fill="#fff"/>
    <g fill="#fff">
      <path d="M61 934a5 5 0 1 1 10 0c0 4-5 9-5 9s-5-5-5-9z"/>
      <path d="M304 934a5 5 0 1 1 10 0c0 4-5 9-5 9s-5-5-5-9z"/>
      <path d="M527 934a5 5 0 1 1 10 0c0 4-5 9-5 9s-5-5-5-9z"/>
    </g>
  </svg>

  <p class="abs brand">Northfield Financial</p>
  <h1 class="abs headline">APPLY HERE<br>FOR <span class="amount">$5,000-$6,000</span><br>TODAY</h1>
  <p class="abs offer-lead">File your taxes<br>&amp; apply for<strong>AN EASY<br>ADVANCE</strong></p>
  <h2 class="abs selling-point">SAME DAY TAX<br>ADVANCE UP TO<span class="big">$6,000</span></h2>
  <p class="abs feature-label" style="left:52px">Availableln<br>24 Hours or Less</p>
  <p class="abs feature-label" style="left:286px">Choose Your<br>Loan Amount</p>
  <p class="abs feature-label" style="left:514px">Quick &amp;<br>Easy</p>
  <p class="abs call">Call Us: +0555 0142 00</p>
  <p class="abs branch" style="left:56px"><b>BROOKVALE – MAIN STREET</b>2210 Oak Hollow Rd<br>Brookvale, TX 78001</p>
  <p class="abs branch" style="left:300px"><b>EASTPORT</b>880 Cedar Ln Ste #120<br>Eastport, TX 78102</p>
  <p class="abs branch" style="left:523px"><b>HILLCREST</b>415 Pine Ridge Dr<br>#210</p>
</main>
</body>
</html>
```